7 P's for Healthcare Companies - Textbook Graphic

Can you create a graphic for me for a medical textbook? The goal is to show 7 critical features of a healthcare startup and the audience is physicians with limited business backgrounds.

Please include a picture of young, male emergency physician in the middle of the graphic. Show them evaluating an idea. Can you surround the physician with bold writing for the seven components, and use brief descriptions and simple images or graphics to illustrate the point?

The image should be somewhat formal, but it's OK to be lighthearded.

The seven P's and brief descriptions include the following:
Product: what is their market solution?
(Intellectual) Property: do they have a patent or trademark?
Product Clearance: how will they get QRB approval and TPW clearance?
Payment: how will they make money?
Pilots: have they applied their product in a healthcare setting?
Physician and Patient feedback: Do doctors and patients like their product?
Publication: do they have evidence their product works?

More detail and information is available at this website: https://brenvolt.com/blog/uncategorized/healthcare-framework/

I will need to own this image

```html
<!DOCTYPE html>
<html lang="en">
<head>
<meta charset="utf-8">
<title>7P – Critical Features of a Healthcare Startup</title>
<link rel="stylesheet" href="https://fonts.googleapis.com/css2?family=Bebas+Neue&family=Barlow+Condensed:wght@500;600;700&family=Barlow:wght@400;500&display=swap">
<style>
  :root {
    --bg: #ffffff;
    --product: #87abc0;
    --clearance: #5f7a8a;
    --pilots: #6cc08b;
    --property: #16bcd6;
    --payment: #1a8fd9;
    --feedback: #0f5fd6;
    --publication: #14318f;
    --title-blue: #1f70d2;
    --seven-blue: #1d5fc0;
    --body-grey: #6b7a86;
    --photo-a: #e9eef2;
    --photo-b: #c9d3da;
    --ink: #1b1b1b;
  }
  * { margin: 0; padding: 0; box-sizing: border-box; }
  html, body { width: 1200px; height: 1200px; overflow: hidden; background: var(--bg); }
  .canvas { position: relative; width: 1200px; height: 1200px; }
  .wheel { position: absolute; left: 0; top: 0; }
  .segment-label {
    font-family: "Barlow Condensed", sans-serif; font-weight: 600;
    font-size: 15px; fill: #fff; text-anchor: middle; letter-spacing: .3px;
  }
  .segment-label.light { font-weight: 500; }
  .segment-label.strong { font-weight: 700; }
  .hub-number {
    position: absolute; left: 0; width: 1200px; top: 476px; text-align: center;
    font-family: "Bebas Neue", sans-serif; font-size: 96px; line-height: 1;
    color: var(--seven-blue);
  }
  .hub-title {
    position: absolute; left: 0; width: 1200px; top: 580px; text-align: center;
    font-family: "Bebas Neue", sans-serif; font-size: 36px; line-height: 39px;
    color: var(--title-blue); letter-spacing: .3px; text-transform: uppercase;
  }
  .physician-photo {
    position: absolute; left: 496px; top: 686px; width: 196px; height: 275px;
    background: linear-gradient(180deg, var(--photo-a), var(--photo-b));
    border-radius: 6px;
  }
  .brand-name {
    position: absolute; left: 674px; top: 934px;
    font-family: "Barlow Condensed", sans-serif; font-weight: 700; font-size: 20px;
    line-height: 1; color: var(--ink);
  }
  .callout { position: absolute; display: flex; align-items: flex-start; gap: 8px; }
  .callout.left { text-align: right; }
  .callout .num {
    font-family: "Bebas Neue", sans-serif; font-size: 66px; line-height: .78;
  }
  .callout .title {
    font-family: "Barlow Condensed", sans-serif; font-weight: 700; font-size: 16px;
    text-transform: uppercase; line-height: 1.1; letter-spacing: .3px;
  }
  .callout .title .light { font-weight: 500; }
  .callout .desc {
    font-family: "Barlow", sans-serif; font-size: 13.5px; color: var(--body-grey); line-height: 1.2;
  }
  .c-pilots { right: 887px; top: 394px; }
  .c-clearance { right: 887px; top: 598px; }
  .c-product { right: 887px; top: 804px; }
  .c-property { left: 512px; top: 286px; }
  .c-payment { left: 890px; top: 410px; }
  .c-feedback { left: 890px; top: 602px; }
  .c-publication { left: 890px; top: 804px; }
  .c-product .num, .c-product .title { color: var(--product); }
  .c-clearance .num, .c-clearance .title { color: var(--clearance); }
  .c-pilots .num, .c-pilots .title { color: var(--pilots); }
  .c-property .num, .c-property .title { color: var(--property); }
  .c-payment .num, .c-payment .title { color: var(--payment); }
  .c-feedback .num, .c-feedback .title { color: var(--feedback); }
  .c-publication .num, .c-publication .title { color: var(--publication); }
  .icon { fill: none; stroke: #fff; stroke-width: 2.4; stroke-linecap: round; stroke-linejoin: round; }
  .icon-fill { fill: #fff; }
</style>
</head>
<body>
<div class="canvas">
  <svg class="wheel" width="1200" height="1200" viewBox="0 0 1200 1200">
    <defs>
      <path id="sector" d="M491.5 348 L708.5 348 L657.6 468 L542.4 468 Z"/>
    </defs>
    <use href="#sector" fill="var(--property)"/>
    <use href="#sector" fill="var(--payment)" transform="rotate(45 600 620)"/>
    <use href="#sector" fill="var(--feedback)" transform="rotate(90 600 620)"/>
    <use href="#sector" fill="var(--publication)" transform="rotate(135 600 620)"/>
    <use href="#sector" fill="var(--product)" transform="rotate(225 600 620)"/>
    <use href="#sector" fill="var(--clearance)" transform="rotate(270 600 620)"/>
    <use href="#sector" fill="var(--pilots)" transform="rotate(315 600 620)"/>

    <!-- intellectual property: certificate -->
    <g class="icon" transform="translate(600 388)">
      <rect x="-18" y="-18" width="36" height="28" rx="2"/>
      <line x1="-10" y1="-9" x2="10" y2="-9"/><line x1="-10" y1="-2" x2="4" y2="-2"/>
      <circle cx="10" cy="8" r="6"/>
    </g>
    <text class="segment-label light" x="600" y="428">INTELLECTUAL</text>
    <text class="segment-label strong" x="600" y="446">PROPERTY</text>

    <!-- payment: banknote in hand -->
    <g class="icon" transform="translate(762 454)">
      <rect x="-12" y="-18" width="30" height="18" rx="2"/>
      <circle cx="3" cy="-9" r="4"/>
      <path d="M-20 8 h10 l8 6 h12 l8 -8"/>
    </g>
    <text class="segment-label" x="735" y="496">PAYMENT</text>

    <!-- feedback: thumbs up -->
    <g class="icon" transform="translate(820 572)">
      <path d="M-16 0 h6 v20 h-6 z"/>
      <path d="M-10 2 l8 -12 v-6 a4 4 0 0 1 6 2 l-2 10 h12 a3 3 0 0 1 3 4 l-3 16 a3 3 0 0 1 -3 2 h-21"/>
      <circle cx="16" cy="-14" r="6"/>
    </g>
    <text class="segment-label" x="822" y="620">PHYSICIAN</text>
    <text class="segment-label" x="822" y="638">&amp; PATIENT</text>
    <text class="segment-label" x="822" y="656">FEEDBACK</text>

    <!-- publication: document with tick -->
    <g class="icon" transform="translate(742 752)">
      <path d="M-14 -20 h18 l8 8 v30 h-26 z"/>
      <line x1="-8" y1="-8" x2="4" y2="-8"/><line x1="-8" y1="-1" x2="4" y2="-1"/>
      <circle cx="10" cy="14" r="7"/><path d="M7 14 l2 2 l4 -4"/>
    </g>
    <text class="segment-label" x="766" y="794">PUBLICATION</text>

    <!-- product: connected cube -->
    <g class="icon" transform="translate(460 752)">
      <path d="M0 -10 l10 5 v11 l-10 5 l-10 -5 v-11 z"/>
      <circle cx="-18" cy="-18" r="3"/><circle cx="18" cy="-18" r="3"/>
      <circle cx="-18" cy="18" r="3"/><circle cx="18" cy="18" r="3"/>
      <line x1="-15" y1="-15" x2="-9" y2="-8"/><line x1="15" y1="-15" x2="9" y2="-8"/>
      <line x1="-15" y1="15" x2="-9" y2="9"/><line x1="15" y1="15" x2="9" y2="9"/>
    </g>
    <text class="segment-label" x="436" y="794">PRODUCT</text>

    <!-- clearance: badge with tick -->
    <g transform="translate(388 574)">
      <path class="icon-fill" d="M0 -20 l6 5 l8 -1 l1 8 l6 5 l-5 6 l2 8 l-8 2 l-4 7 l-6 -4 l-6 4 l-4 -7 l-8 -2 l2 -8 l-5 -6 l6 -5 l1 -8 l8 1 z"/>
      <path d="M-7 0 l5 5 l9 -10" fill="none" stroke="var(--clearance)" stroke-width="3" stroke-linecap="round" stroke-linejoin="round"/>
    </g>
    <text class="segment-label" x="388" y="622">PRODUCT</text>
    <text class="segment-label" x="388" y="640">CLEARANCE</text>

    <!-- pilots: heart with plus over hand -->
    <g class="icon" transform="translate(438 454)">
      <path d="M-4 6 c-10 -8 -14 -12 -14 -18 a6 6 0 0 1 12 -2 a6 6 0 0 1 12 2 c0 6 -4 10 -10 18 z"/>
      <path d="M12 -18 v10 M7 -13 h10"/>
      <path d="M-20 14 h10 l8 5 h12 l8 -7"/>
    </g>
    <text class="segment-label" x="466" y="496">PILOTS</text>
  </svg>

  <div class="hub-number">7P</div>
  <div class="hub-title">Critical features of<br>a healthcare startup</div>

  <div class="physician-photo" role="img" aria-label="Photo of a young male emergency physician in a white coat with a stethoscope, holding a tablet while evaluating an idea"></div>
  <div class="brand-name">Brenvolt</div>

  <div class="callout left c-pilots">
    <div><div class="title">Pilots</div><div class="desc">Have they applied their product<br>in a healthcare setting?</div></div>
    <div class="num">3</div>
  </div>
  <div class="callout left c-clearance">
    <div><div class="title">Product Clearance</div><div class="desc">How will they get QRB approval<br>and TPW clearance?</div></div>
    <div class="num">2</div>
  </div>
  <div class="callout left c-product">
    <div><div class="title">Product</div><div class="desc">What is their market solution?</div></div>
    <div class="num">1</div>
  </div>
  <div class="callout c-property">
    <div class="num">4</div>
    <div><div class="title"><span class="light">Intellectual</span> Property</div><div class="desc">Do they have a patent or trademark?</div></div>
  </div>
  <div class="callout c-payment">
    <div class="num">5</div>
    <div><div class="title">Payment</div><div class="desc">How will they make money?</div></div>
  </div>
  <div class="callout c-feedback">
    <div class="num">6</div>
    <div><div class="title">Physician &amp; Patient Feedback</div><div class="desc">Do doctors and patients<br>like their product?</div></div>
  </div>
  <div class="callout c-publication">
    <div class="num">7</div>
    <div><div class="title">Publication</div><div class="desc">Do they have evidence<br>their product works?</div></div>
  </div>
</div>
</body>
</html>
```